Landing Page for Bathroom Remodeling Webpage - Desktop and Mobile

I am looking for some help designing the "above the fold" area for my bathroom remodeling service page. Looking for something a little different than the rest. Typically remodeling companies just put a nice picture of a bathroom remodel but I would like to do something a little different / more creative. Below is a link to the current wireframe we are working on.
Current website is located at plumvantaridge.com
Again the biggest thing I am looking for is a design for the very top section but would love help on the rest of the page as well. You will see by viewing the link below the type of information we are looking to include on the page:
PLEASE DO INCLUDE WHAT THE MOBILE VERSION WOULD LOOK LIKE AS WELL.
Wireframe:
https://boards.quillmerra.com/view/3f8a1b2c-90de-4e7a-b5c1-aa62d09e1f35-418k/
There are also comments in the link above you can read as well.
We like the idea of something interactive such as this...
https://pixorvale.com/shots/5192746-Glenhart-Scooter-Store-Animation
Attached is also the logo we want to use going forward
Target Market(s)
Residential homeowners, 30 years old+ with professional careers
Number of Pages Required
1 page
Look and feel
Each slider illustrates characteristics of the customer's brand and the style your logo design should communicate.

```html
<!DOCTYPE html>
<html lang="en">
<head>
<meta charset="utf-8">
<title>Plumvanta – Bathroom Remodeling Landing Page</title>
<link href="https://fonts.googleapis.com/css2?family=Roboto:wght@400;500;700&family=Open+Sans:wght@400;600&display=swap" rel="stylesheet">
<style>
:root{
  --navy:#1b2b5f;
  --navy-deep:#15234f;
  --hero:#1d4aa8;
  --red:#c8102e;
  --orange:#f04e1d;
  --grey-bg:#efefef;
  --ink:#222;
  --muted:#666;
  --white:#fff;
}
*{margin:0;padding:0;box-sizing:border-box}
html,body{width:1200px;height:3123px;overflow:hidden;background:var(--white)}
body{position:relative;font-family:"Open Sans",sans-serif;color:var(--ink)}
.abs{position:absolute}
.head{font-family:"Roboto",sans-serif}
.brand{font-family:"Roboto",sans-serif;font-weight:700;color:var(--red);display:flex;align-items:center;gap:6px;letter-spacing:.3px}
.brand-dot{border-radius:50%;background:var(--navy)}
.section-title{font-family:"Roboto",sans-serif;font-weight:500;text-decoration:underline;text-underline-offset:3px;color:var(--ink);text-align:center;text-transform:uppercase}
.section-title em{font-style:normal;color:var(--red)}
.photo{position:absolute}
.small{font-size:7px;color:var(--muted);line-height:1.6}
.nav a{font-family:"Roboto",sans-serif;font-size:7px;font-weight:500;color:var(--ink);text-decoration:none;margin-right:14px}
.card{background:var(--white);text-align:center;font-family:"Open Sans",sans-serif}
.card h4{font-family:"Roboto",sans-serif;font-size:10px;font-weight:500;margin:6px 0 3px}
.card p{font-size:7px;color:var(--muted);line-height:1.9}
.price-col{text-align:center}
.price-col h3{font-family:"Roboto",sans-serif;font-size:11px;color:var(--red);font-weight:700}
.price-col .sub{font-size:7px;color:var(--muted);margin-top:8px;line-height:1.6}
.price-bar{height:32px;margin-top:12px;color:var(--white);font-family:"Roboto",sans-serif;font-weight:700;font-size:20px;display:flex;align-items:center;justify-content:center;border-radius:2px}
.price-bar sup{font-size:8px;margin-right:2px}
.price-list{font-size:7px;color:var(--muted);line-height:2;margin-top:26px}
.learn{display:inline-block;margin-top:20px;width:70px;height:20px;line-height:20px;border-radius:10px;background:var(--navy);color:#fff;font-size:6px;font-weight:700;font-family:"Roboto",sans-serif}
.faq-row{border-bottom:1px solid #ddd;font-size:7px;color:var(--muted);padding:8px 0;display:flex;justify-content:space-between}
.field{background:#f5f5f5;font-size:7px;color:#888;padding:6px 8px}
.foot-col h5{font-family:"Roboto",sans-serif;font-size:8px;font-weight:700;color:var(--navy);margin-bottom:12px}
.foot-col p{font-size:6.5px;color:var(--muted);line-height:2.6}
.social{display:flex;gap:5px}
.social span{width:13px;height:13px;border-radius:50%;background:var(--navy);display:block}
.copy{background:var(--navy);color:#fff;font-size:7px;text-align:center}
.dots{display:flex;gap:4px;justify-content:center}
.dots i{width:3px;height:3px;border-radius:50%;background:#bbb;display:block}
</style>
</head>
<body>

<!-- ================= DESKTOP ================= -->
<header class="abs" style="left:120px;top:0;width:664px;height:46px">
  <div class="brand abs" style="left:6px;top:12px;font-size:19px"><span class="brand-dot" style="width:18px;height:18px"></span>PLUMVANTA</div>
  <nav class="nav abs" style="left:208px;top:18px"><a>HOME ⌄</a><a>SERVICES ⌄</a><a>ABOUT</a><a>CONTACT ⌄</a><a>BLOG ⌄</a><a>GALLERY ⌄</a><a>VIDEOS ⌄</a></nav>
  <div class="abs" style="left:580px;top:5px;width:84px;height:27px;background:var(--navy);color:#fff;font-family:Roboto,sans-serif;font-size:7px;text-align:center;line-height:1.2;padding-top:7px">GET AN ESTIMATE<br>515-555-0142</div>
</header>

<section class="abs" style="left:120px;top:50px;width:664px;height:372px">
  <div class="photo" role="img" aria-label="Bathroom with freestanding tub tinted in deep blue" style="inset:0;background:linear-gradient(180deg,#1e50b4 0%,#1a45a0 60%,#163a88 100%)"></div>
  <div class="abs" style="left:0;top:278px;width:664px;height:94px;background:rgba(10,30,80,.25)"></div>
  <p class="abs head" style="left:93px;top:132px;color:#fff;font-size:11px;letter-spacing:1.6px;line-height:1.75;font-weight:500">IT'S WHERE YOU START AND END YOUR DAY. A BATHROOM REMODEL<br>WILL MAKE SURE IT STARTS AND ENDS RIGHT.</p>
  <h1 class="abs head" style="left:93px;top:172px;color:#fff;font-size:25px;line-height:1.15;font-weight:700;letter-spacing:.8px;text-decoration:underline;text-underline-offset:4px">BATHROOM REMODELING</h1>
  <div class="abs head" style="left:93px;top:222px;color:#fff;font-size:6px;display:flex;align-items:center;gap:4px">DETAILS
    <svg width="40" height="20" viewBox="0 0 40 20"><circle cx="10" cy="10" r="9" fill="none" stroke="#fff" stroke-width=".8"/><path d="M4 10H36M32 7l4 3-4 3" stroke="#fff" fill="none" stroke-width="1"/></svg></div>
  <div class="abs head" style="left:608px;top:157px;color:#cfd8ee;font-size:7px;line-height:3.4">01<br><span style="color:var(--red)">—</span><br>03</div>
  <p class="abs head" style="left:93px;top:328px;color:#fff;font-size:5.5px;letter-spacing:1px;word-spacing:6px">JOURNAL UPDATES PORTFOLIO</p>
</section>

<h2 class="section-title abs" style="left:120px;top:454px;width:664px;font-size:20px"><em>GET INSPIRED BY</em> SIMILAR PROJECTS</h2>
<div class="photo" role="img" aria-label="Modern bathroom with oval mirror and black vanity" style="left:196px;top:498px;width:513px;height:229px;background:linear-gradient(90deg,#c9c9c9,#e6e6e6 40%,#8f8f8f 70%,#d8d8d8)"></div>
<span class="abs" style="left:202px;top:606px;color:#fff;font-size:10px">‹</span><span class="abs" style="left:698px;top:606px;color:#fff;font-size:10px">›</span>
<div class="photo" role="img" aria-label="Bathroom thumbnail" style="left:196px;top:740px;width:92px;height:52px;background:linear-gradient(#b7b7b7,#7b7b7b)"></div>
<div class="photo" role="img" aria-label="Bathroom thumbnail" style="left:301px;top:740px;width:92px;height:52px;background:linear-gradient(#5e5a55,#8e8882)"></div>
<div class="photo" role="img" aria-label="Bathroom thumbnail" style="left:407px;top:740px;width:92px;height:52px;background:linear-gradient(#e5e5e5,#9bc45a)"></div>
<div class="photo" role="img" aria-label="Bathroom thumbnail" style="left:512px;top:740px;width:92px;height:52px;background:linear-gradient(#9a9a9a,#3d3d3d)"></div>
<div class="photo" role="img" aria-label="Bathroom thumbnail" style="left:617px;top:740px;width:92px;height:52px;background:linear-gradient(#d3d3d3,#888)"></div>

<section class="abs" style="left:116px;top:821px;width:672px;height:345px;background:var(--grey-bg)">
  <h2 class="section-title abs" style="left:80px;top:26px;font-size:19px;text-align:left"><em>MATERIAL</em> SELECTIONS</h2>
  <p class="abs small" style="left:80px;top:60px;width:260px">For your bathroom remodel there will be material selections you will have to make. Use the lists below to get an idea of some of the options.</p>
  <div class="photo" role="img" aria-label="Grey marble bathroom with clawfoot tub" style="left:90px;top:102px;width:230px;height:182px;background:linear-gradient(135deg,#8a8a8a,#d0d0d0 50%,#6d6d6d)"></div>
  <div class="card abs" style="left:346px;top:32px;width:115px;height:129px;padding-top:20px">
    <svg width="18" height="18" viewBox="0 0 18 18"><path d="M5 4a7 7 0 1 0 8 0" fill="none" stroke="var(--navy)" stroke-width="2"/><path d="M9 1v8" stroke="var(--navy)" stroke-width="2"/></svg>
    <h4>Electrical</h4><p>Light Fixtures<br>Heated Floor<br>Outlets</p></div>
  <div class="card abs" style="left:472px;top:32px;width:116px;height:129px;padding-top:20px">
    <svg width="18" height="18" viewBox="0 0 18 18"><path d="M3 3l12 12M15 3L3 15" stroke="var(--navy)" stroke-width="3" stroke-linecap="round"/></svg>
    <h4>Plumbing</h4><p>Vanity Fixtures<br>Shower Fixtures<br>Toilet</p></div>
  <div class="card abs" style="left:346px;top:170px;width:115px;height:142px;padding-top:20px">
    <svg width="14" height="16" viewBox="0 0 14 16"><g fill="var(--navy)"><rect x="1" y="1" width="5" height="4"/><rect x="8" y="1" width="5" height="4"/><rect x="1" y="6" width="5" height="4"/><rect x="8" y="6" width="5" height="4"/><rect x="1" y="11" width="5" height="4"/><rect x="8" y="11" width="5" height="4"/></g></svg>
    <h4>Tile &amp; Flooring</h4><p>Shower Wall Tile<br>Shower Floor Tile<br>Bathroom Flooring</p></div>
  <div class="card abs" style="left:472px;top:170px;width:116px;height:142px;padding-top:20px">
    <svg width="18" height="18" viewBox="0 0 18 18"><path d="M16 2L8 11" stroke="var(--navy)" stroke-width="3" stroke-linecap="round"/><path d="M7 11c-3 0-4 2-4 5 3 0 6-1 6-4z" fill="var(--navy)"/></svg>
    <h4>Finishes</h4><p>Trim<br>Mirrors &amp; Towel Bars<br>Cabinetry &amp; Counter<br>Tops</p></div>
</section>

<section class="abs" style="left:120px;top:1171px;width:664px;height:127px">
  <div class="photo" role="img" aria-label="Dark grey bathroom interior" style="inset:0;background:linear-gradient(90deg,#4a5268,#6a7186 50%,#3e465c)"></div>
  <div class="abs" style="left:0;top:0;width:0;height:0;border-top:40px solid var(--red);border-right:40px solid transparent"></div>
  <h3 class="abs head" style="left:0;top:32px;width:664px;text-align:center;color:#fff;font-size:11px;font-weight:500">Schedule A Free In Home Consultation Via Our Online Appointment Scheduling System</h3>
  <p class="abs" style="left:0;top:54px;width:664px;text-align:center;color:#fff;font-size:7px">Lorem ipsum dolor sit amet consectetur adipiscing elit dolor</p>
  <div class="abs head" style="left:304px;top:72px;width:58px;height:18px;border:1px solid #fff;color:#fff;font-size:6.5px;text-align:center;line-height:16px">SCHEDULE</div>
</section>

<h2 class="section-title abs" style="left:120px;top:1330px;width:664px;font-size:19px"><em>PRICING</em> PACKAGES</h2>
<div class="abs" style="left:365px;top:1368px;width:175px;height:268px;background:var(--grey-bg)"></div>
<div class="price-col abs" style="left:196px;top:1373px;width:164px"><h3>Minor Upgrades</h3><p class="sub">Perfect for changing out some fixtures.</p>
  <div class="price-bar" style="background:var(--red);margin-top:12px"><sup>$</sup>$</div>
  <p class="price-list">Shower Fixtures<br>Vanity Fixtures<br>Mirrors / Towel Bars<br>Tile</p><span class="learn">Learn more</span></div>
<div class="price-col abs" style="left:370px;top:1373px;width:165px"><h3>Moderate Remodel</h3><p class="sub">Complete remodel with layout staying the same.</p>
  <div class="price-bar" style="background:var(--orange)"><sup>$</sup>$$</div>
  <p class="price-list">Shower Fixtures<br>Vanity Fixtures<br>Mirrors / Towel Bars<br>Tile<br>Cabinetry<br>Countertops</p><span class="learn">Learn more</span></div>
<div class="price-col abs" style="left:544px;top:1373px;width:165px"><h3>Major Remodel</h3><p class="sub">Complete remodel with new layout. This is a gut job.</p>
  <div class="price-bar" style="background:var(--red)"><sup>$</sup>$$$</div>
  <p class="price-list">Shower Fixtures<br>Vanity Fixtures<br>Mirrors / Towel Bars<br>Tile<br>Cabinetry<br>Countertops<br>Re-Route Plumbing / Electrical<br>Move Walls</p><span class="learn">Learn more</span></div>

<section class="abs" style="left:116px;top:1668px;width:672px;height:269px;background:var(--grey-bg)">
  <h2 class="section-title abs" style="left:0;top:30px;width:672px;font-size:19px"><em>HELPFUL</em> ARTICLES</h2>
  <div class="card abs" style="left:84px;top:65px;width:161px;height:171px">
    <div class="photo" role="img" aria-label="Worker laying floor tiles" style="left:18px;top:24px;width:125px;height:82px;background:linear-gradient(135deg,#d8d2c8,#8d8477)"></div>
    <h4 class="abs" style="left:10px;top:110px;width:141px;font-size:10px;line-height:1.25">Home Remodeling Made Easier with Simple Tips</h4></div>
  <div class="card abs" style="left:256px;top:65px;width:161px;height:171px">
    <div class="photo" role="img" aria-label="Bright room under renovation with ladder" style="left:18px;top:24px;width:125px;height:70px;background:linear-gradient(135deg,#eaeaea,#9a9a9a)"></div>
    <h4 class="abs" style="left:10px;top:98px;width:141px;font-size:10px;line-height:1.25">Keeping Costs Reasonable When Planning Whole Home Remodeling</h4></div>
  <div class="card abs" style="left:428px;top:65px;width:160px;height:171px">
    <div class="photo" role="img" aria-label="Handshake over building plans" style="left:18px;top:24px;width:124px;height:56px;background:linear-gradient(135deg,#b9c8dc,#5a6f8e)"></div>
    <h4 class="abs" style="left:10px;top:86px;width:140px;font-size:10px;line-height:1.25">Handyman vs. Contractor – Who Should You Call?</h4></div>
</section>

<h2 class="section-title abs" style="left:120px;top:1964px;width:664px;font-size:19px"><em>FREQUENTLY</em> ASKED QUESTIONS</h2>
<div class="photo" role="img" aria-label="Round white basin with brass wall tap and flowers" style="left:196px;top:1997px;width:171px;height:347px;background:linear-gradient(160deg,#e9e4dd,#bfb6aa 60%,#6f6658)"></div>
<div class="photo" role="img" aria-label="Navy bathroom with round mirror and plant" style="left:367px;top:1997px;width:171px;height:347px;background:linear-gradient(180deg,#2f3f78,#1d2c5c)"></div>
<h3 class="abs head" style="left:380px;top:2138px;color:#fff;font-size:18px;font-weight:500;line-height:1.2">Frequently<br>Asked<br>Questions</h3>
<div class="abs" style="left:542px;top:1997px;width:166px">
  <div class="faq-row" style="color:var(--ink)"><span>Can I Customize The Section Color?</span><b>–</b></div>
  <p class="small" style="font-size:6.5px;padding:6px 0">Ut elit tellus, luctus nec ullamcorper mattis, pulvinar dapibus leo. Lorem ipsum dolor sit amet, consectetur adipiscing elit. Praesent tempor congue pretium. Aliquam libero ante, eleifend vel ligula vitae, fermentum rutrum eros. Nam quis vestibulum ligula. Aliquam erat volutpat. Worrying does not empty tomorrow of its troubles, it empties today of its strength.</p>
  <p class="small" style="font-size:6.5px;padding:4px 0 8px">Ut elit tellus, luctus nec ullamcorper mattis, pulvinar dapibus leo. Lorem ipsum dolor sit amet, consectetur adipiscing elit. Praesent tempor congue pretium. Aliquam libero ante, eleifend vel ligula vitae, fermentum rutrum eros. Nam quis vestibulum ligula. Aliquam erat volutpat. Worrying does not empty tomorrow of its troubles, it empties today of its strength.</p>
  <div class="faq-row"><span>How To Insert The Block To The Page?</span><b>+</b></div>
  <div class="faq-row"><span>How Long The Support Period?</span><b>+</b></div>
  <div class="faq-row"><span>How Can I Update The Template?</span><b>+</b></div>
  <div class="faq-row"><span>Can I Downgrade The Plan?</span><b>+</b></div>
  <div class="faq-row"><span>Where Can I Find The CSS Selectors?</span><b>+</b></div>
</div>

<section class="abs" style="left:116px;top:2372px;width:672px;height:474px;background:var(--grey-bg)">
  <h2 class="section-title abs" style="left:0;top:22px;width:672px;font-size:19px"><em>HOW TO</em> FIND US</h2>
  <div class="abs" style="left:75px;top:76px;width:523px;height:78px;background:var(--navy);color:#fff">
    <div class="abs" style="left:18px;top:18px;display:flex;gap:10px">
      <svg width="26" height="26" viewBox="0 0 26 26"><circle cx="13" cy="13" r="13" fill="#fff"/><path d="M13 6a4.5 4.5 0 0 0-4.5 4.5C8.5 14 13 20 13 20s4.5-6 4.5-9.5A4.5 4.5 0 0 0 13 6z" fill="var(--navy)"/><circle cx="13" cy="10.5" r="1.6" fill="#fff"/></svg>
      <div><b class="head" style="font-size:10px;font-weight:500">Address</b><p style="font-size:7px;line-height:1.6;margin-top:4px">4410 Larkmoor Ave Ste B Dalecrest,<br>IA 50390</p></div></div>
    <div class="abs" style="left:180px;top:18px;display:flex;gap:10px">
      <svg width="26" height="26" viewBox="0 0 26 26"><circle cx="13" cy="13" r="13" fill="#fff"/><path d="M9 7l3 3-2 2c1 2 2 3 4 4l2-2 3 3-2 2c-5 0-10-5-10-10z" fill="var(--navy)"/></svg>
      <div><b class="head" style="font-size:10px;font-weight:500">Phone</b><p style="font-size:7px;margin-top:4px">515-555-0142</p></div></div>
    <div class="abs" style="left:342px;top:18px;display:flex;gap:10px">
      <svg width="26" height="26" viewBox="0 0 26 26"><circle cx="13" cy="13" r="13" fill="#fff"/><rect x="7" y="9" width="12" height="9" fill="var(--navy)"/><path d="M7 9l6 5 6-5" stroke="#fff" fill="none"/></svg>
      <div><b class="head" style="font-size:10px;font-weight:500">Email</b><p style="font-size:7px;line-height:1.9;margin-top:4px">info@plumvantaridge.com<br>support@plumvantaridge.com</p></div></div>
  </div>
  <div class="abs" style="left:75px;top:154px;width:262px;height:294px;background:#fff;padding:20px 22px">
    <h3 class="head" style="font-size:11px;font-weight:500;margin-bottom:14px">Book Your Appointment</h3>
    <div class="field" style="margin-bottom:12px">Your Name</div>
    <div class="field" style="margin-bottom:12px">Your Email</div>
    <div class="field" style="margin-bottom:12px">Your Phone Number</div>
    <div class="field" style="height:100px">Message</div>
    <div style="margin-top:8px;width:68px;height:20px;background:var(--navy);color:#fff;font-size:6.5px;text-align:center;line-height:20px;font-family:Roboto,sans-serif">Send Request</div>
  </div>
  <div class="photo" role="img" aria-label="Street map with office location pin" style="left:337px;top:154px;width:261px;height:294px;background:linear-gradient(135deg,#eef0ea,#e2e6df)"></div>
  <svg class="abs" style="left:460px;top:292px" width="14" height="20" viewBox="0 0 14 20"><path d="M7 0a7 7 0 0 0-7 7c0 5 7 13 7 13s7-8 7-13a7 7 0 0 0-7-7z" fill="var(--red)"/><circle cx="7" cy="7" r="2.5" fill="#8b0b1f"/></svg>
</section>

<footer class="abs" style="left:116px;top:2880px;width:672px;height:160px">
  <div class="brand abs" style="left:80px;top:12px;font-size:20px"><span class="brand-dot" style="width:22px;height:22px"></span>PLUMVANTA</div>
  <p class="abs small" style="left:80px;top:52px;width:170px;font-size:6.5px">I am text block. Click edit button to change this text. Lorem ipsum dolor sit amet, consectetur adipiscing elit. Ut elit tellus, luctus nec ullamcorper matti pibus leo.</p>
  <div class="social abs" style="left:124px;top:100px"><span></span><span></span><span></span><span></span></div>
  <div class="foot-col abs" style="left:288px;top:8px"><h5>GET STARTED</h5><p><span style="color:var(--red)">Home</span><br>About<br>Services<br>Reviews<br>Contact Us</p></div>
  <div class="foot-col abs" style="left:393px;top:8px"><h5>SERVICES</h5><p>Bathroom Remodeling<br>Basement Finishing<br>Kitchen Remodeling<br>Window Replacement<br>Whole Home Remodeling</p></div>
  <div class="foot-col abs" style="left:497px;top:8px"><h5>SERVICE AREAS</h5><p style="line-height:2.3">Ankeny, IA<br>Clive, IA<br>Des Moines, IA<br>Johnston, IA<br>Urbandale, IA<br>Waukee, IA<br>West Des Moines, IA</p></div>
</footer>
<div class="copy abs" style="left:116px;top:3045px;width:672px;height:78px;padding-top:24px">Copyright © 2021 PLUMVANTA | Powered by PLUMVANTA</div>

<!-- ================= MOBILE ================= -->
<div class="brand abs" style="left:846px;top:12px;font-size:20px"><span class="brand-dot" style="width:22px;height:22px"></span>PLUMVANTA</div>
<div class="abs" style="left:1024px;top:56px;width:16px;height:11px;border:1px solid #ccc"></div>
<div class="abs head" style="left:840px;top:76px;width:203px;height:22px;background:var(--navy);color:#fff;font-size:6px;text-align:center;line-height:1.25;padding-top:4px">GET AN ESTIMATE<br>515-555-0142</div>
<section class="abs" style="left:840px;top:108px;width:203px;height:202px">
  <div class="photo" role="img" aria-label="Bathroom with freestanding tub tinted in deep blue" style="inset:0;background:linear-gradient(180deg,#1e50b4,#163a88)"></div>
  <p class="abs head" style="left:8px;top:70px;color:#fff;font-size:4.5px;line-height:1.6;width:150px">IT'S WHERE YOU START AND END YOUR DAY. A BATHROOM REMODEL WILL MAKE SURE IT STARTS AND ENDS RIGHT.</p>
  <h1 class="abs head" style="left:8px;top:94px;color:#fff;font-size:11px;line-height:1.2;font-weight:700;text-decoration:underline">BATHROOM REMODELING</h1>
  <p class="abs head" style="left:8px;top:120px;color:#fff;font-size:5px">DETAILS ○⟶</p>
  <p class="abs head" style="left:182px;top:152px;color:#cfd8ee;font-size:5px;line-height:3"><span>01</span><br><span style="color:var(--red)">02</span><br>03</p>
  <p class="abs head" style="left:8px;top:186px;color:#fff;font-size:4px;word-spacing:4px">JOURNAL UPDATES PORTFOLIO</p>
</section>
<h2 class="section-title abs" style="left:840px;top:338px;width:210px;font-size:10px;text-align:left"><em>GET INSPIRED BY</em> SIMILAR PROJECTS</h2>
<div class="photo" role="img" aria-label="Dark tiled bathroom with tub and vanity" style="left:840px;top:371px;width:203px;height:179px;background:linear-gradient(135deg,#6d6a66,#bdbab4 50%,#4d4a46)"></div>
<div class="dots abs" style="left:840px;top:556px;width:203px"><i></i><i></i><i></i><i></i><i></i><i></i></div>

<section class="abs" style="left:836px;top:588px;width:210px;height:394px;background:var(--grey-bg)">
  <h2 class="section-title abs" style="left:0;top:25px;width:210px;font-size:10px"><em>MATERIAL</em> SELECTIONS</h2>
  <p class="abs small" style="left:4px;top:46px;width:202px;font-size:5px">For your bathroom remodel there will be material selections you will have to make. Use the lists below to get an idea of some of the options.</p>
  <div class="photo" role="img" aria-label="Grey marble bathroom with clawfoot tub" style="left:4px;top:84px;width:203px;height:160px;background:linear-gradient(135deg,#8a8a8a,#d0d0d0 50%,#6d6d6d)"></div>
  <div class="abs" style="left:4px;top:252px;width:203px;height:84px;background:#fff;padding:8px 30px">
    <h4 class="head" style="font-size:10px;font-weight:500">Finishes</h4>
    <p class="small" style="font-size:5.5px;margin-top:8px;padding-left:14px;line-height:2">Trim<br>Mirrors &amp; Towel Bars</p>
    <p class="small" style="font-size:5.5px;margin-left:-6px">Cabinetry &amp; Counter Tops</p></div>
  <div class="dots abs" style="left:0;top:351px;width:210px"><i></i><i></i><i></i><i style="background:var(--red)"></i></div>
</section>
<section class="abs" style="left:840px;top:988px;width:203px;height:116px">
  <div class="photo" role="img" aria-label="Dark grey bathroom interior" style="inset:0;background:linear-gradient(90deg,#3e4a6e,#55607e)"></div>
  <div class="abs" style="left:0;top:0;border-top:34px solid var(--red);border-right:34px solid transparent"></div>
  <h3 class="abs head" style="left:10px;top:20px;width:183px;text-align:center;color:#fff;font-size:9px;font-weight:500;line-height:1.25">Schedule A Free In Home Consultation Via Our Online Appointment Scheduling System</h3>
  <p class="abs" style="left:0;top:63px;width:203px;text-align:center;color:#fff;font-size:5px">Lorem ipsum dolor sit amet consectetur adipiscing elit dolor</p>
  <div class="abs" style="left:80px;top:80px;width:42px;height:11px;border:1px solid #fff;color:#fff;font-size:4.5px;text-align:center;line-height:9px">SCHEDULE</div>
</section>
<h2 class="section-title abs" style="left:836px;top:1134px;width:210px;font-size:10px"><em>PRICING</em> PACKAGES</h2>
<section class="abs" style="left:840px;top:1156px;width:203px;height:201px;background:var(--navy);color:#fff">
  <p class="abs" style="left:26px;top:38px;font-size:6px">Complete remodel with layout staying the same</p>
  <p class="abs head" style="left:26px;top:56px;font-size:7px;font-weight:700;text-decoration:underline">Moderate Remodel</p>
  <div class="abs" style="left:26px;top:80px;width:50px;height:16px;border:1px solid #fff;border-radius:8px;font-size:5px;line-height:14px;padding-left:8px">Details ⟶</div>
  <p class="abs" style="left:42px;top:112px;font-size:5px;line-height:1.6">Shower Fixtures<br>✓Vanity Fixtures<br>✓Mirrors / Towel Bars<br>✓Tile<br>✓Cabinetry<br>✓Countertops</p>
  <p class="abs" style="left:176px;top:86px;font-size:4px;transform:rotate(90deg);transform-origin:left top">Read More</p>
  <div class="abs" style="left:14px;top:180px;display:flex;gap:8px;align-items:center"><i style="width:3px;height:3px;border-radius:50%;background:#fff;display:block"></i><i style="width:6px;height:6px;border-radius:50%;border:1.5px solid #fff;display:block"></i><i style="width:3px;height:3px;border-radius:50%;background:#fff;display:block"></i></div>
  <p class="abs" style="left:154px;top:175px;font-size:8px">○ ○</p>
</section>
<section class="abs" style="left:836px;top:1382px;width:210px;height:272px;background:var(--grey-bg)">
  <h2 class="section-title abs" style="left:0;top:24px;width:210px;font-size:10px"><em>HELPFUL</em> ARTICLES</h2>
  <div class="photo" role="img" aria-label="Bright room under renovation tinted blue" style="left:4px;top:46px;width:203px;height:202px;background:linear-gradient(135deg,#5677b8,#203c7c)"></div>
  <p class="abs head" style="left:34px;top:128px;width:143px;color:#fff;font-size:5.5px;text-align:center;font-weight:700;line-height:1.8">Keeping Costs Reasonable When Planning Whole Home Remodeling</p>
  <div class="abs" style="left:86px;top:160px;width:40px;height:12px;border:1px solid #fff;border-radius:6px;color:#fff;font-size:4.5px;line-height:10px;text-align:center">Details ⟶</div>
</section>
<h2 class="section-title abs" style="left:836px;top:1680px;width:210px;font-size:10px"><em>FREQUENTLY</em> ASKED QUESTIONS</h2>
<div class="photo" role="img" aria-label="Navy bathroom banner" style="left:840px;top:1700px;width:203px;height:45px;background:linear-gradient(90deg,#1d2c5c,#3a4a80)"></div>
<p class="abs head" style="left:856px;top:1716px;color:#fff;font-size:9.5px;font-weight:500">Frequently Asked Questions</p>
<div class="abs" style="left:844px;top:1750px;width:195px;font-size:5.5px">
  <div class="faq-row" style="font-size:5.5px;color:var(--ink)"><span>Can I Customize The Section Color?</span><b>–</b></div>
  <p class="small" style="font-size:5px;padding:5px 0">Ut elit tellus, luctus nec ullamcorper mattis, pulvinar dapibus leo. Lorem ipsum dolor sit amet, consectetur adipiscing elit. Praesent tempor congue pretium. Aliquam libero ante, eleifend vel ligula vitae, fermentum rutrum eros. Nam quis vestibulum ligula. Aliquam erat volutpat. Worrying does not empty tomorrow of its troubles, it empties today of its strength.</p>
  <p class="small" style="font-size:5px;padding:3px 0 6px">Ut elit tellus, luctus nec ullamcorper mattis, pulvinar dapibus leo. Lorem ipsum dolor sit amet, consectetur adipiscing elit. Praesent tempor congue pretium. Aliquam libero ante, eleifend vel ligula vitae, fermentum rutrum eros. Nam quis vestibulum ligula. Aliquam erat volutpat. Worrying does not empty tomorrow of its troubles, it empties today of its strength.</p>
  <div class="faq-row" style="font-size:5px;padding:6px 0"><span>How To Insert The Block To The Page?</span><b>+</b></div>
  <div class="faq-row" style="font-size:5px;padding:6px 0"><span>How Long The Support Period?</span><b>+</b></div>
  <div class="faq-row" style="font-size:5px;padding:6px 0"><span>How Can I Update The Template?</span><b>+</b></div>
  <div class="faq-row" style="font-size:5px;padding:6px 0"><span>Can I Downgrade The Plan?</span><b>+</b></div>
  <div class="faq-row" style="font-size:5px;padding:6px 0"><span>Where Can I Find The CSS Selectors?</span><b>+</b></div>
</div>
<h2 class="section-title abs" style="left:836px;top:2052px;width:210px;font-size:10px"><em>HOW TO</em> FIND US</h2>
<div class="abs" style="left:836px;top:2066px;width:210px;height:26px;background:var(--grey-bg)"></div>
<section class="abs" style="left:836px;top:2092px;width:210px;height:256px;background:var(--navy);color:#fff;text-align:center">
  <svg class="abs" style="left:96px;top:16px" width="18" height="18" viewBox="0 0 18 18"><circle cx="9" cy="9" r="9" fill="#fff"/><path d="M9 4a3 3 0 0 0-3 3c0 2.5 3 6 3 6s3-3.5 3-6a3 3 0 0 0-3-3z" fill="var(--navy)"/></svg>
  <p class="abs head" style="left:0;top:42px;width:210px;font-size:8px;font-weight:500">Address</p>
  <p class="abs" style="left:50px;top:56px;width:110px;font-size:5.5px;line-height:1.7">4410 Larkmoor Ave Ste B Dalecrest, IA 50390</p>
  <svg class="abs" style="left:96px;top:100px" width="18" height="18" viewBox="0 0 18 18"><circle cx="9" cy="9" r="9" fill="#fff"/><path d="M6 5l2 2-1 1.5c.7 1.4 1.5 2.2 2.5 2.7L11 10l2 2-1.5 1.5C8 13.5 4.5 10 4.5 6.5z" fill="var(--navy)"/></svg>
  <p class="abs head" style="left:0;top:128px;width:210px;font-size:8px;font-weight:500">Phone</p>
  <p class="abs" style="left:0;top:142px;width:210px;font-size:5.5px">515-555-0142</p>
  <svg class="abs" style="left:96px;top:172px" width="18" height="18" viewBox="0 0 18 18"><circle cx="9" cy="9" r="9" fill="#fff"/><rect x="5" y="6" width="8" height="6" fill="var(--navy)"/></svg>
  <p class="abs head" style="left:0;top:200px;width:210px;font-size:8px;font-weight:500">Email</p>
  <p class="abs" style="left:0;top:214px;width:210px;font-size:5.5px;line-height:1.9">info@plumvantaridge.com<br>support@plumvantaridge.com</p>
</section>
<section class="abs" style="left:840px;top:2360px;width:203px">
  <h3 class="head" style="font-size:9px;font-weight:500;margin:4px 14px 10px">Book Your Appointment</h3>
  <div class="field" style="margin:0 6px 9px 6px;font-size:5px;padding:4px 6px">Your Name</div>
  <div class="field" style="margin:0 6px 9px 6px;font-size:5px;padding:4px 6px">Your Email</div>
  <div class="field" style="margin:0 6px 9px 6px;font-size:5px;padding:4px 6px">Your Phone Number</div>
  <div class="field" style="margin:0 6px 0 6px;font-size:5px;padding:4px 6px;height:92px">Message</div>
  <div style="margin:12px 0 0 8px;width:48px;height:16px;background:var(--navy);color:#fff;font-size:5px;text-align:center;line-height:16px">Send Request</div>
</section>
<div class="photo" role="img" aria-label="Street map with office location pin" style="left:836px;top:2611px;width:210px;height:179px;background:linear-gradient(135deg,#eef0ea,#e2e6df)"></div>
<svg class="abs" style="left:935px;top:2695px" width="11" height="16" viewBox="0 0 14 20"><path d="M7 0a7 7 0 0 0-7 7c0 5 7 13 7 13s7-8 7-13a7 7 0 0 0-7-7z" fill="var(--red)"/></svg>

<div class="brand abs" style="left:846px;top:2812px;font-size:20px"><span class="brand-dot" style="width:22px;height:22px"></span>PLUMVANTA</div>
<p class="abs small" style="left:844px;top:2858px;width:198px;font-size:5px">I am text block. Click edit button to change this text. Lorem ipsum dolor sit amet, consectetur adipiscing elit. Ut elit tellus, luctus nec ullamcorper matti pibus leo.</p>
<div class="abs" style="left:844px;top:2909px;display:flex;gap:3px"><i style="width:9px;height:9px;border-radius:50%;background:var(--navy);display:block"></i><i style="width:9px;height:9px;border-radius:50%;background:var(--navy);display:block"></i><i style="width:9px;height:9px;border-radius:50%;background:var(--navy);display:block"></i><i style="width:9px;height:9px;border-radius:50%;background:var(--navy);display:block"></i></div>
<div class="foot-col abs" style="left:844px;top:2938px"><h5 style="font-size:6px;margin-bottom:8px">GET STARTED</h5><p style="font-size:8px">≡</p></div>
<div class="foot-col abs" style="left:908px;top:2938px"><h5 style="font-size:6px;margin-bottom:6px">SERVICES</h5><p style="font-size:4.5px;line-height:2.4">Bathroom Remodeling<br>Basement Finishing<br>Kitchen Remodeling<br>Window Replacement<br>Whole Home Remodeling</p></div>
<div class="foot-col abs" style="left:974px;top:2938px"><h5 style="font-size:6px;margin-bottom:6px">SERVICE AREAS</h5><p style="font-size:4.5px;line-height:2.4">Ankeny, IA<br>Clive, IA<br>Des Moines, IA<br>Johnston, IA<br>Urbandale, IA<br>Waukee, IA<br>West Des Moines, IA</p></div>
<div class="copy abs" style="left:836px;top:3046px;width:210px;height:77px;font-size:5.5px;padding-top:34px">Copyright © 2021 PLUMVANTA | Powered by PLUMVANTA</div>

</body>
</html>
```